Copper Gavel Auctions business card design with existing logo

Looking for a sleek and sexy design using our current logo

Contact Information for Business Card

Name, address, email, phone, website. Marcus Delvane 418 Birchmont Road Suite 200C Fenwick NY 11093 Copperbidhouse.net (631)582-4067

```html
<!DOCTYPE html>
<html lang="en">
<head>
<meta charset="utf-8">
<title>Copper Gavel Auctions – Business Card</title>
<link rel="stylesheet" href="https://fonts.googleapis.com/css2?family=Roboto:wght@400;700&display=swap">
<style>
  :root {
    --navy: #1b3f7a;
    --red: #d0202b;
    --ink: #1d1d1f;
    --paper: #ffffff;
    --backdrop: #1e1e1e;
  }
  * { margin: 0; padding: 0; box-sizing: border-box; }
  html, body { width: 1200px; height: 1059px; overflow: hidden; }
  body { background: var(--backdrop); font-family: "Roboto", sans-serif; position: relative; }

  .card { position: absolute; border-radius: 20px; overflow: hidden; }

  .card-front { left: 257px; top: 89px; width: 687px; height: 390px; background: var(--paper); }
  .card-front .base-band { position: absolute; left: 0; right: 0; bottom: 0; height: 10px; background: var(--navy); }

  .brand { position: absolute; display: flex; flex-direction: column; align-items: center; text-align: center; }
  .brand-dot { border-radius: 50%; background: var(--red); }
  .brand-name { font-weight: 700; letter-spacing: 0.08em; line-height: 1.15; text-transform: uppercase; }

  .card-front .brand { left: 80px; top: 130px; width: 240px; }
  .card-front .brand-dot { width: 58px; height: 58px; margin-bottom: 16px; }
  .card-front .brand-name { font-size: 21px; color: var(--navy); }

  .divider { position: absolute; left: 342px; top: 110px; width: 2px; height: 171px; background: var(--red); }

  .contact { position: absolute; left: 373px; top: 104px; color: var(--ink); }
  .person-name { font-size: 28px; font-weight: 700; color: var(--navy); line-height: 1.1; }
  .person-name .surname { color: var(--red); }
  .person-role { font-size: 16px; margin-top: 4px; }
  .address { font-size: 16px; line-height: 20px; margin-top: 15px; }
  .details { list-style: none; margin-top: 12px; font-size: 16px; }
  .details li { display: flex; align-items: center; height: 22px; }
  .details svg { width: 11px; height: 11px; margin-right: 6px; fill: var(--navy); }

  .card-back { left: 254px; top: 547px; width: 693px; height: 393px; background: var(--navy); }
  .card-back .brand { left: 0; right: 0; top: 95px; }
  .card-back .brand-dot { width: 96px; height: 96px; margin-bottom: 26px; }
  .card-back .brand-name { font-size: 32px; color: var(--paper); }
</style>
</head>
<body>
  <section class="card card-front">
    <div class="brand">
      <div class="brand-dot"></div>
      <div class="brand-name">Copper Gavel<br>Auctions</div>
    </div>
    <div class="divider"></div>
    <div class="contact">
      <h1 class="person-name">MARCUS <span class="surname">DELVANE</span></h1>
      <p class="person-role">CEO/Founder</p>
      <p class="address">418 Birchmont Road Suite<br>200C Fenwick NY 11093</p>
      <ul class="details">
        <li><svg viewBox="0 0 12 12"><path d="M2 1h2l1 3-1.5 1a7 7 0 0 0 3.5 3.5L8 7l3 1v2a1 1 0 0 1-1 1C5 11 1 7 1 2a1 1 0 0 1 1-1z"/></svg>(631)582-4067</li>
        <li><svg viewBox="0 0 12 12"><path d="M0 2h12v1L6 7 0 3z M0 4.5l6 4 6-4V10H0z"/></svg>info@copperbidhouse.net</li>
        <li><svg viewBox="0 0 12 12"><circle cx="6" cy="6" r="5.5"/></svg>www.copperbidhouse.net</li>
      </ul>
    </div>
    <div class="base-band"></div>
  </section>

  <section class="card card-back">
    <div class="brand">
      <div class="brand-dot"></div>
      <div class="brand-name">Copper Gavel<br>Auctions</div>
    </div>
  </section>
</body>
</html>
```